Kestrel Bathrooms

Fix our flyer add as the one we got made has the wrong phone number on it would like different photos on it

Want it to Stand out and be in your face!

I will attach our logo
phone number is 0487265903
Email is Miles@kestrelbathrooms.com.au

happy to keep all prices the same

If you can make it better happy to tip $$

```html
<!DOCTYPE html>
<html lang="en">
<head>
<meta charset="utf-8">
<title>Kestrel Bathrooms Flyer</title>
<link rel="stylesheet" href="https://fonts.googleapis.com/css2?family=Oswald:wght@500;600&family=Montserrat:wght@500;600;700&family=Libre+Baskerville&family=Great+Vibes&display=swap">
<style>
  :root {
    --blue: #1565b8;
    --ink: #1b1b1b;
    --grey-band: #d4d4d4;
    --foot: #eef0f4;
    --icon: #b9bcc2;
    --white: #ffffff;
  }
  html, body { margin: 0; padding: 0; overflow: hidden; background: var(--white); }
  .flyer { position: relative; width: 965px; height: 1200px; overflow: hidden; background: var(--white); font-family: "Montserrat", sans-serif; }
  .layer { position: absolute; inset: 0; }
  .brand { position: absolute; left: 41px; top: 88px; display: flex; align-items: center; gap: 12px; }
  .brand-square { width: 22px; height: 22px; background: var(--blue); }
  .brand-name { font-family: "Montserrat", sans-serif; font-weight: 700; font-size: 32px; color: var(--blue); letter-spacing: 0.5px; white-space: nowrap; }
  .headline { position: absolute; left: 41px; top: 228px; margin: 0; font-family: "Oswald", sans-serif; font-weight: 600; font-size: 54px; line-height: 55px; color: var(--blue); text-transform: uppercase; }
  .band-script { position: absolute; left: 41px; top: 455px; font-family: "Great Vibes", cursive; font-size: 42px; color: var(--ink); }
  .band-title { position: absolute; left: 41px; top: 494px; margin: 0; font-family: "Oswald", sans-serif; font-weight: 500; font-size: 48px; line-height: 58px; color: var(--blue); }
  .services-intro { position: absolute; left: 41px; top: 568px; font-family: "Libre Baskerville", serif; font-size: 19px; color: var(--ink); }
  .service { position: absolute; display: flex; align-items: center; gap: 8px; font-weight: 600; font-size: 24px; color: var(--blue); }
  .service-icon { width: 18px; height: 18px; border: 2px solid var(--icon); border-radius: 4px; box-sizing: border-box; }
  .package-photo { position: absolute; top: 823px; width: 282px; height: 267px; }
  .package { position: absolute; top: 758px; width: 230px; text-align: center; color: var(--white); }
  .package-tag { display: inline-block; background: var(--white); color: var(--blue); font-family: "Oswald", sans-serif; font-weight: 500; font-size: 16px; line-height: 22px; padding: 0 10px; }
  .package-name { margin: 6px 0 0; font-family: "Oswald", sans-serif; font-weight: 500; font-size: 21px; line-height: 25px; text-transform: uppercase; }
  .package-from { font-size: 11px; line-height: 14px; margin-top: 2px; }
  .package-price { font-family: "Oswald", sans-serif; font-weight: 500; font-size: 32px; line-height: 38px; }
  .contact-title { position: absolute; left: 0; width: 965px; top: 1062px; text-align: center; font-family: "Great Vibes", cursive; font-size: 38px; color: var(--blue); }
  .contact-phone { position: absolute; left: 0; width: 965px; top: 1105px; text-align: center; font-size: 29px; font-weight: 500; color: var(--ink); display: flex; justify-content: center; align-items: center; gap: 8px; }
  .contact-links { position: absolute; left: 0; width: 965px; top: 1153px; display: flex; justify-content: center; gap: 36px; font-size: 20px; font-weight: 500; color: var(--ink); }
  .contact-links span { display: flex; align-items: center; gap: 7px; }
</style>
</head>
<body>
<main class="flyer">
  <svg class="layer" width="965" height="1200" viewBox="0 0 965 1200">
    <defs>
      <linearGradient id="roomTones" x1="0" y1="0" x2="1" y2="1">
        <stop offset="0" stop-color="#7a5a44"/>
        <stop offset="0.45" stop-color="#b48b6c"/>
        <stop offset="0.8" stop-color="#d9d2c9"/>
        <stop offset="1" stop-color="#ece9e5"/>
      </linearGradient>
    </defs>
    <polygon points="600,0 632,0 330,289 965,900 965,940 287,289" fill="var(--blue)"/>
    <polygon points="640,0 965,0 965,900 330,289" fill="url(#roomTones)" role="img" aria-label="Bathroom interior with timber cabinetry, marble wall panels, pendant lights and a floating vanity"/>
    <polygon points="0,455 540,455 600,555 0,555" fill="var(--grey-band)"/>
  </svg>

  <div class="brand"><span class="brand-square"></span><span class="brand-name">Kestrel Bathrooms</span></div>

  <h1 class="headline">Illawarra<br>based and<br>family<br>operated</h1>

  <div class="band-script">Kestrel Bathrooms</div>
  <h2 class="band-title">FULLY LICENSED &amp; INSURED</h2>

  <div class="services-intro">Built To Last Your Local Renovation Specialist:</div>
  <div class="service" style="left:41px;top:597px"><span class="service-icon"></span>DEMOLITION</div>
  <div class="service" style="left:259px;top:597px"><span class="service-icon"></span>ELECTRICAL</div>
  <div class="service" style="left:472px;top:597px"><span class="service-icon"></span>TILING</div>
  <div class="service" style="left:41px;top:635px"><span class="service-icon"></span>PLUMBING</div>
  <div class="service" style="left:259px;top:635px"><span class="service-icon"></span>DESIGN CONSULTATION</div>
  <div class="service" style="left:41px;top:672px"><span class="service-icon"></span>CARPENTRY</div>
  <div class="service" style="left:259px;top:672px"><span class="service-icon"></span>WATERPROOFING</div>

  <div class="package-photo" style="left:41px;background:linear-gradient(135deg,#7b5a42,#c9a98c 55%,#dcd6cf)" role="img" aria-label="Main bathroom with marble wall, timber panelling and floating vanity"></div>
  <div class="package-photo" style="left:342px;background:linear-gradient(135deg,#cfd4da,#eef0f2 60%,#ffffff)" role="img" aria-label="Bright ensuite with white vanity, mirror and freestanding bath"></div>
  <div class="package-photo" style="left:642px;background:linear-gradient(135deg,#e6e3df,#f4f2ef 50%,#b88a5c)" role="img" aria-label="Laundry with marble splashback, basins and stacked washer and dryer in timber joinery"></div>

  <svg class="layer" width="965" height="1200" viewBox="0 0 965 1200">
    <polygon points="182,714 297,825 182,935 67,825" fill="var(--blue)"/>
    <polygon points="482,714 597,825 482,935 367,825" fill="var(--blue)"/>
    <polygon points="782,714 897,825 782,935 667,825" fill="var(--blue)"/>
    <polygon points="0,1105 482,1030 965,1105 965,1200 0,1200" fill="var(--foot)"/>
    <polygon points="0,1095 482,1022 965,1095 965,1110 482,1040 0,1110" fill="var(--blue)"/>
    <line x1="0" y1="1175" x2="50" y2="1175" stroke="var(--blue)" stroke-width="3"/>
    <line x1="915" y1="1175" x2="965" y2="1175" stroke="var(--blue)" stroke-width="3"/>
  </svg>

  <div class="package" style="left:67px">
    <span class="package-tag">SAVE UP TO $4,000</span>
    <h3 class="package-name">Main Bathroom<br>Package</h3>
    <div class="package-from">Price Starts From</div>
    <div class="package-price">$18,900</div>
  </div>
  <div class="package" style="left:367px">
    <span class="package-tag">SAVE UP TO $4,000</span>
    <h3 class="package-name">Ensuite<br>Package</h3>
    <div class="package-from">Price Starts From</div>
    <div class="package-price">$14,900</div>
  </div>
  <div class="package" style="left:667px">
    <span class="package-tag">SAVE UP TO $4,000</span>
    <h3 class="package-name">Laundry<br>Package</h3>
    <div class="package-from">Price Starts From</div>
    <div class="package-price">$9,900</div>
  </div>

  <div class="contact-title">Contact Us</div>
  <div class="contact-phone">
    <svg width="24" height="24" viewBox="0 0 24 24"><path d="M6.6 10.8a15 15 0 0 0 6.6 6.6l2.2-2.2a1 1 0 0 1 1-.25 11.4 11.4 0 0 0 3.6.6 1 1 0 0 1 1 1V20a1 1 0 0 1-1 1A17 17 0 0 1 3 4a1 1 0 0 1 1-1h3.5a1 1 0 0 1 1 1c0 1.25.2 2.45.6 3.6a1 1 0 0 1-.25 1z" fill="var(--blue)"/></svg>
    Call us at 0487 265 903
  </div>
  <div class="contact-links">
    <span><svg width="22" height="22" viewBox="0 0 22 22"><circle cx="11" cy="11" r="9.5" fill="none" stroke="var(--blue)" stroke-width="2"/><ellipse cx="11" cy="11" rx="4" ry="9.5" fill="none" stroke="var(--blue)" stroke-width="1.6"/><line x1="1.5" y1="11" x2="20.5" y2="11" stroke="var(--blue)" stroke-width="1.6"/></svg>www.kestrelbathrooms.com.au</span>
    <span><svg width="24" height="18" viewBox="0 0 24 18"><rect x="1" y="1" width="22" height="16" fill="none" stroke="var(--blue)" stroke-width="2"/><polyline points="1,1 12,10 23,1" fill="none" stroke="var(--blue)" stroke-width="2"/></svg>Miles@kestrelbathrooms.com.au</span>
  </div>
</main>
</body>
</html>
```